Dalton Power Supply, Inc. Business Card Design

We are an Electrical Distributor looking for a Modern, Professional Business Card design.

Target Market(s)

Residential Commercial Industrial

Industry/Entity Type

Electrical

Contact Information for Business Card

Dalton Power Supply, Inc.
418 Maple Ridge Lane
Brookvale, NC 27514
555-214-7630
555-214-8842 Fax
daltonpower@brightmail-example.net

```html
<!DOCTYPE html>
<html lang="en">
<head>
<meta charset="utf-8">
<title>Dalton Power Supply, Inc. – Business Card</title>
<link rel="stylesheet" href="https://fonts.googleapis.com/css2?family=Montserrat:wght@700&family=Didact+Gothic&display=swap">
<style>
  :root {
    --backdrop: #2a2c2a;
    --card: #ffffff;
    --brand-blue: #1f5dab;
    --ink: #1c1c1c;
  }
  * { margin: 0; padding: 0; box-sizing: border-box; }
  html, body {
    width: 1200px;
    height: 1039px;
    overflow: hidden;
    background: var(--backdrop);
  }
  .business-card {
    position: absolute;
    left: 100px;
    top: 234px;
    width: 1000px;
    height: 571px;
    overflow: hidden;
    background: var(--card);
    font-family: "Didact Gothic", "Century Gothic", sans-serif;
    color: var(--ink);
  }
  .company-name {
    position: absolute;
    left: 52px;
    top: 112px;
    font-family: "Montserrat", sans-serif;
    font-weight: 700;
    font-size: 40px;
    line-height: 1.1;
    color: var(--brand-blue);
    letter-spacing: 0.5px;
  }
  .brand-mark {
    position: absolute;
    left: 640px;
    top: 50px;
    width: 470px;
    height: 470px;
    border-radius: 50%;
    background: var(--brand-blue);
  }
  .person {
    position: absolute;
    left: 80px;
    top: 305px;
  }
  .person-name {
    font-family: "Montserrat", sans-serif;
    font-weight: 700;
    font-size: 28px;
    color: var(--brand-blue);
  }
  .person-title {
    font-size: 24px;
    margin-top: 2px;
  }
  .contact-list {
    position: absolute;
    left: 80px;
    top: 398px;
    list-style: none;
    font-size: 26px;
    line-height: 36px;
  }
  .contact-list li {
    display: flex;
    align-items: center;
    gap: 12px;
    white-space: nowrap;
  }
  .contact-icon {
    width: 26px;
    height: 22px;
    fill: var(--brand-blue);
    flex: none;
  }
  .address {
    position: absolute;
    left: 80px;
    top: 515px;
    font-size: 26px;
    white-space: nowrap;
    word-spacing: 0;
  }
</style>
</head>
<body>
  <article class="business-card">
    <h1 class="company-name">Dalton Power<br>Supply, Inc.</h1>

    <div class="brand-mark" role="img" aria-label="Large brand mark for Dalton Power Supply"></div>

    <div class="person">
      <p class="person-name">Your Name</p>
      <p class="person-title">Job Title</p>
    </div>

    <ul class="contact-list">
      <li>
        <svg class="contact-icon" viewBox="0 0 26 22" aria-hidden="true">
          <path d="M2 7c0-3 5-5 11-5s11 2 11 5v2h-6V6.5c-3-1-7-1-10 0V9H2z"/>
          <path d="M6 10h14l3 10H3z"/>
          <circle cx="13" cy="15" r="3" fill="#fff"/>
        </svg>
        <span>555-214-7630</span>
      </li>
      <li>
        <svg class="contact-icon" viewBox="0 0 26 22" aria-hidden="true">
          <rect x="7" y="1" width="12" height="7"/>
          <rect x="2" y="8" width="22" height="9" rx="2"/>
          <rect x="7" y="14" width="12" height="7" fill="#fff" stroke="#1f5dab" stroke-width="2"/>
        </svg>
        <span>555-214-8842</span>
      </li>
      <li>
        <svg class="contact-icon" viewBox="0 0 26 22" aria-hidden="true">
          <rect x="1" y="3" width="24" height="16"/>
          <path d="M1 3l12 9 12-9M1 19l9-8M25 19l-9-8" fill="none" stroke="#fff" stroke-width="1.6"/>
        </svg>
        <span>daltonpower@brightmail-example.net</span>
      </li>
    </ul>

    <p class="address">418 Maple Ridge Lane, Brookvale, NC 27514</p>
  </article>
</body>
</html>
```